Book cover for book about Climate Change

Looking for a clean, bold, and attractive cover for a mass-market paperback (5.5"x 8.5") about solving the climate change problem. Title is either "When Rivers Learn to Sing” or A Lantern Over Quiet Fields” (your choice), subtitle is "A five-step plan to reverse climate change — to ensure that your grandchildren will live on a clean and comfortable planet," author is Dale Pruitt. Thinking that it *might* feature an image of Earth (or a portion thereof) and its very thin layer of atmosphere -- but STRONGLY encourage other ideas too!

Requirements
Nice to have
• Keep it positive — NOT scary doom-and-gloom

```html
<!DOCTYPE html>
<html lang="en">
<head>
<meta charset="utf-8">
<title>A Lantern Over Quiet Fields — Dale Pruitt</title>
<link href="https://fonts.googleapis.com/css2?family=Anton&family=Montserrat:wght@400;700;800&display=swap" rel="stylesheet">
<style>
  :root {
    --paper-light: #f0f2e4;
    --paper-mid: #e1e8cf;
    --paper-edge: #c6d3aa;
    --forest-deep: #0e3512;
    --forest: #1d5a1c;
    --leaf: #2f8a22;
    --leaf-light: #86c23a;
    --ink-green: #1a4416;
    --ocean: #5d9fb4;
    --ocean-light: #a9d2dc;
    --land: #7f9a5c;
  }
  html, body {
    margin: 0;
    padding: 0;
    overflow: hidden;
    background: #ffffff;
  }
  .cover {
    position: relative;
    width: 775px;
    height: 1200px;
    overflow: hidden;
    background:
      radial-gradient(ellipse at 50% 45%, var(--paper-light) 0%, var(--paper-mid) 55%, var(--paper-edge) 100%);
  }
  .title {
    position: absolute;
    top: 62px;
    left: 0;
    width: 100%;
    margin: 0;
    text-align: center;
    font-family: "Anton", "Oswald", sans-serif;
    font-weight: 400;
    text-transform: uppercase;
    line-height: 1.12;
    letter-spacing: 0.5px;
  }
  .title-line {
    display: block;
    font-size: 98px;
    -webkit-background-clip: text;
    background-clip: text;
    color: transparent;
  }
  .title-line--top {
    background-image: linear-gradient(180deg, var(--forest-deep) 0%, var(--forest) 100%);
  }
  .title-line--bottom {
    background-image: linear-gradient(180deg, var(--leaf) 0%, var(--leaf-light) 100%);
  }
  .subtitle {
    position: absolute;
    top: 362px;
    left: 0;
    width: 100%;
    margin: 0;
    text-align: center;
    font-family: "Montserrat", sans-serif;
    color: var(--ink-green);
  }
  .subtitle-lead {
    display: block;
    font-weight: 700;
    font-size: 20px;
    letter-spacing: 0.2px;
    text-transform: uppercase;
    margin-bottom: 4px;
  }
  .subtitle-rest {
    display: block;
    font-weight: 400;
    font-size: 20.5px;
    line-height: 1.5;
  }
  .globe-art {
    position: absolute;
    left: 116px;
    top: 500px;
    width: 544px;
    height: 544px;
  }
  .author {
    position: absolute;
    top: 1080px;
    left: 0;
    width: 100%;
    margin: 0;
    text-align: center;
    font-family: "Montserrat", sans-serif;
    font-weight: 800;
    font-size: 50px;
    letter-spacing: 5px;
    color: var(--ink-green);
    text-transform: uppercase;
  }
</style>
</head>
<body>
  <main class="cover">
    <h1 class="title">
      <span class="title-line title-line--top">A Lantern Over</span>
      <span class="title-line title-line--bottom">Quiet Fields</span>
    </h1>

    <p class="subtitle">
      <span class="subtitle-lead">A five-step plan to reverse climate change</span>
      <span class="subtitle-rest">to ensure that your grandchildren will<br>live on a clean and comfortable planet</span>
    </p>

    <svg class="globe-art" viewBox="0 0 544 544" role="img"
         aria-label="Illustration of planet Earth holding an hourglass: penguins on ice in the upper bulb, smokestacks in the lower bulb">
      <defs>
        <radialGradient id="globe-fill" cx="45%" cy="40%" r="60%">
          <stop offset="0%" stop-color="var(--ocean-light)"/>
          <stop offset="60%" stop-color="var(--ocean)"/>
          <stop offset="100%" stop-color="var(--land)"/>
        </radialGradient>
      </defs>
      <circle cx="272" cy="272" r="272" fill="url(#globe-fill)"/>
    </svg>

    <p class="author">Dale Pruitt</p>
  </main>
</body>
</html>
```